Design a New Site for a very cool Watch

We have the overall design element of the website and the banners in the PSD file. We need someone to finish our design in PSD and than convert to HTML. We have included the instructions, PSD file, images and all text.

We currently use Hubspot to host and make changes to our site. The entire design aspect is complete so all we need is some minor changes and additions within the photoshop design and than the coding into HTML.

Please only sign up if you understand photoshop and HTML conversion

Here is the DropBox link to the files
https://files.quorvel-share.net/s/pm4kx82lwq7dtne/Belthor%20Site.zip
Updates

We have the basic design concept in Photoshop.  We just need someone who can complete some changes, make some additions and convert to HTML

Target Market(s)

Watch Buyers

Requirements
Must have
• Must look like a professional luxury brand

Our brand colors are very basic with Black, White and Grey can be used

```html
<!DOCTYPE html>
<html lang="en">
<head>
<meta charset="utf-8">
<title>Belthor &amp; Co. — Watches</title>
<link rel="stylesheet" href="https://fonts.googleapis.com/css2?family=Cormorant+Garamond:wght@400;500;600&family=Cinzel:wght@400&family=Arimo:wght@400&display=swap">
<style>
  :root {
    --ink: #000000;
    --white: #ffffff;
    --panel: #4b4b4b;
    --button: #3a3a3a;
    --button-edge: #5a5a5a;
    --frame: #d9d9d9;
    --bar: #5c5c5c;
    --link-blue: #4e8fe0;
    --search-fill: #9a9a9a;
    --social: #2a7fd4;
  }
  * { box-sizing: border-box; margin: 0; padding: 0; }
  html, body { width: 1200px; height: 943px; overflow: hidden; background: var(--ink); }
  body { position: relative; font-family: "Cormorant Garamond", Georgia, serif; color: var(--white); }
  .abs { position: absolute; }
  a { color: inherit; text-decoration: none; }

  .backdrop { left: 0; top: 330px; width: 1200px; height: 613px;
    background: radial-gradient(ellipse 620px 360px at 600px 430px, #6a6a6a 0%, #3a3a3a 40%, #111 75%, #000 100%); }
  .planet-glow { left: 880px; top: 0; width: 320px; height: 230px;
    background: radial-gradient(circle at 220px 95px, #e8ecff 0%, #7a86ff 10%, #2a2f7a 28%, rgba(0,0,0,0) 60%); }

  .brand { left: 190px; top: 54px; font-family: "Cinzel", Georgia, serif; font-size: 34px; letter-spacing: 1px; color: var(--white); white-space: nowrap; }

  .search-label { left: 691px; top: 14px; font-family: "Arimo", Arial, sans-serif; font-size: 16px; color: var(--link-blue); }
  .search-box { left: 754px; top: 12px; width: 172px; height: 19px; background: var(--search-fill); border: 1px solid #bbb; }
  .shop-line { left: 691px; top: 41px; font-family: "Arimo", Arial, sans-serif; font-size: 15px; color: var(--white); white-space: nowrap; }
  .shop-line a { color: var(--link-blue); text-decoration: underline; }

  .nav-btn { display: flex; align-items: center; justify-content: center; background: linear-gradient(#4a4a4a, #2e2e2e);
    border: 1px solid var(--button-edge); border-radius: 3px; font-size: 31px; color: var(--white); white-space: nowrap; }
  .nav-btn.active { font-size: 37px; }

  .social { top: 199px; width: 16px; height: 16px; background: var(--social); border-radius: 3px; }

  .showcase { left: 188px; top: 220px; width: 824px; height: 269px; background: var(--panel); border-radius: 4px; }
  .hero { left: 198px; top: 227px; width: 410px; height: 255px; border: 1px solid var(--frame);
    background: linear-gradient(135deg, #0c1f44 0%, #c9c9cc 35%, #eeeeee 60%, #8d8a86 100%); }
  .dot { top: 466px; width: 12px; height: 12px; border-radius: 50%; background: var(--white); }
  .dot.off { background: #555; }
  .thumbs { left: 618px; top: 227px; width: 386px; height: 253px; background: var(--ink); border: 1px solid var(--frame); }
  .thumb { width: 116px; height: 104px; border: 1px solid var(--frame); }
  .tone-watch { background: linear-gradient(135deg, #111 0%, #a9a5a0 45%, #e9e6e4 65%, #111 100%); }
  .tone-gem { background: radial-gradient(ellipse at 55% 55%, #d2d4ee 0%, #5a5c80 35%, #000 75%); }
  .tone-dark { background: linear-gradient(135deg, #1a1d44 0%, #4a4f9a 40%, #d0d0d8 60%, #20224a 100%); }

  .tab { top: 508px; width: 171px; height: 38px; background: var(--button); border-radius: 3px; display: flex; align-items: center; justify-content: center; white-space: nowrap; }
  .tab span { font-size: 19px; font-weight: 500; border-bottom: 1px solid var(--white); line-height: 1.1; }

  .card { top: 555px; width: 160px; height: 139px; background: var(--ink); border: 1px solid var(--frame); border-radius: 3px; }
  .card-pic { position: absolute; left: 3px; top: 3px; right: 3px; height: 71px; border: 1px solid var(--frame); }
  .card-text { position: absolute; left: 5px; top: 86px; right: 2px; font-size: 11.5px; line-height: 10.5px; white-space: nowrap; }

  .news { left: 188px; width: 824px; height: 28px; background: var(--bar); border-radius: 4px; font-size: 11px; padding: 8px 5px 0; white-space: nowrap; }
  .news .more { position: absolute; right: 30px; bottom: 3px; font-size: 9px; }

  .foot-link { top: 874px; font-size: 20px; white-space: nowrap; }
  .foot-rule { left: 2px; top: 900px; width: 1192px; height: 4px; background: #8a8a8a; }
  .copyright { left: 532px; top: 907px; font-size: 12px; border-bottom: 1px solid var(--white); white-space: nowrap; }
</style>
</head>
<body>
  <div class="abs backdrop" role="img" aria-label="Field of sparkling crystals and gems reflecting on dark water"></div>
  <div class="abs planet-glow" role="img" aria-label="Glowing edge of a planet with a bright light flare in space"></div>

  <div class="abs brand">BELTHOR &amp; CO.</div>

  <div class="abs search-label">Search</div>
  <div class="abs search-box"></div>
  <div class="abs shop-line">Online Shoping <a href="#">Click Here</a></div>

  <nav>
    <a class="abs nav-btn" style="left:188px;top:154px;width:194px;height:40px;">Home</a>
    <a class="abs nav-btn active" style="left:399px;top:141px;width:192px;height:66px;">Product</a>
    <a class="abs nav-btn" style="left:609px;top:154px;width:194px;height:40px;">Contact</a>
    <a class="abs nav-btn" style="left:818px;top:154px;width:195px;height:40px;">Photo Gallery</a>
  </nav>

  <div class="abs social" style="left:932px;"></div>
  <div class="abs social" style="left:951px;"></div>
  <div class="abs social" style="left:970px;"></div>
  <div class="abs social" style="left:989px;"></div>

  <section class="abs showcase"></section>
  <div class="abs hero" role="img" aria-label="Close-up of a square steel watch with a white dial and floating pink stones"></div>
  <div class="abs dot" style="left:526px;"></div>
  <div class="abs dot off" style="left:547px;"></div>
  <div class="abs dot" style="left:567px;"></div>
  <div class="abs dot" style="left:587px;"></div>

  <div class="abs thumbs"></div>
  <div class="abs thumb tone-watch" style="left:626px;top:236px;" role="img" aria-label="White watch thumbnail"></div>
  <div class="abs thumb tone-gem" style="left:749px;top:236px;" role="img" aria-label="Cut diamond thumbnail"></div>
  <div class="abs thumb tone-dark" style="left:876px;top:236px;" role="img" aria-label="Dark blue watch thumbnail"></div>
  <div class="abs thumb tone-gem" style="left:626px;top:359px;" role="img" aria-label="Cut diamond thumbnail"></div>
  <div class="abs thumb tone-dark" style="left:751px;top:359px;" role="img" aria-label="Dark blue watch thumbnail"></div>
  <div class="abs thumb tone-watch" style="left:876px;top:359px;" role="img" aria-label="White watch thumbnail"></div>

  <div class="abs tab" style="left:187px;"><span>The Orin Story</span></div>
  <div class="abs tab" style="left:395px;"><span>Register your Watch</span></div>
  <div class="abs tab" style="left:617px;"><span>Repair &amp; Warranty</span></div>
  <div class="abs tab" style="left:842px;"><span>Register for More</span></div>

  <article class="abs card" style="left:187px;">
    <div class="card-pic tone-watch" role="img" aria-label="White watch on black"></div>
    <p class="card-text">We develop very unique mens and<br>womans watches<br>We develop very unique mens and<br>womans watches</p>
  </article>
  <article class="abs card" style="left:354px;">
    <div class="card-pic tone-gem" role="img" aria-label="Cut diamond on black"></div>
    <p class="card-text">We develop very unique mens and<br>womans watches<br>We develop very unique mens and<br>womans watches</p>
  </article>
  <article class="abs card" style="left:520px;">
    <div class="card-pic tone-dark" role="img" aria-label="Dark blue watch on black"></div>
    <p class="card-text">We develop very unique mens and<br>womans watches<br>We develop very unique mens and<br>womans watches</p>
  </article>
  <article class="abs card" style="left:687px;">
    <div class="card-pic tone-watch" role="img" aria-label="White watch on black"></div>
    <p class="card-text">We develop very unique mens and<br>womans watches<br>We develop very unique mens and<br>womans watches</p>
  </article>
  <article class="abs card" style="left:853px;">
    <div class="card-pic tone-gem" role="img" aria-label="Cut diamond on black"></div>
    <p class="card-text">We develop very unique mens and<br>womans watches<br>We develop very unique mens and<br>womans watches</p>
  </article>

  <div class="abs news" style="top:715px;">We develop very unique mens and womans watches. Our first collection, the Orin Watch actually has a real piece of the Moon, Mars and a very rare space Gem inside the watch.<span class="more">&gt;&gt;&gt;</span></div>
  <div class="abs news" style="top:752px;">We develop very unique mens and womans watches. Our first collection, the Orin Watch actually has a real piece of the Moon, Mars and a very rare space Gem inside the watch.<span class="more">&gt;&gt;&gt;</span></div>
  <div class="abs news" style="top:790px;">We develop very unique mens and womans watches. Our first collection, the Orin Watch actually has a real piece of the Moon, Mars and a very rare space Gem inside the watch.<span class="more">&gt;&gt;&gt;</span></div>

  <footer>
    <a class="abs foot-link" style="left:284px;">Home</a>
    <a class="abs foot-link" style="left:401px;">Product</a>
    <a class="abs foot-link" style="left:550px;">Contact</a>
    <a class="abs foot-link" style="left:683px;">Photo Gallery</a>
    <a class="abs foot-link" style="left:841px;">About Us</a>
    <div class="abs foot-rule"></div>
    <div class="abs copyright">2013@All Right Are Reserved</div>
  </footer>
</body>
</html>
```